Business card design needed

It's a new business in town.Something so the name stands out.I need a logo for the B.R.W
I may all so use the design as a sign on a building

Contact Information for Business Card

B.R.W
Brindlewood Auto Detailing
42 Fenwarra Crs
Brindlewood Vic 3799
Ph:(03)59284736
Mob:0417362958

```html
<!DOCTYPE html>
<html lang="en">
<head>
<meta charset="utf-8">
<title>B.R.W Brindlewood Auto Detailing – Business Card</title>
<link rel="stylesheet" href="https://fonts.googleapis.com/css2?family=Questrial&display=swap">
<style>
  :root {
    --brand-orange: #e03f00;
    --band-orange: #e04000;
    --ghost-tint: #fdf0ed;
    --card-white: #ffffff;
  }
  * { margin: 0; padding: 0; box-sizing: border-box; }
  html, body {
    width: 1200px;
    height: 741px;
    overflow: hidden;
    background: var(--card-white);
  }
  .card {
    position: relative;
    width: 1200px;
    height: 741px;
    background: var(--card-white);
    font-family: "Questrial", "Century Gothic", sans-serif;
    overflow: hidden;
  }
  .band {
    position: absolute;
    background: var(--band-orange);
  }
  .band--top { left: 0; top: 0; width: 1200px; height: 19px; }
  .band--bottom { left: 4px; top: 721px; width: 1196px; height: 20px; }
  .name-art {
    position: absolute;
    left: 0;
    top: 0;
    width: 1200px;
    height: 741px;
  }
  .name-art__ghost { fill: var(--ghost-tint); }
  .name-art__mark { fill: var(--brand-orange); }
  .name-art text {
    font-family: "Questrial", "Century Gothic", sans-serif;
  }
  .contact {
    position: absolute;
    left: 538px;
    top: 470px;
    color: var(--brand-orange);
    font-size: 35px;
    line-height: 80px;
    white-space: nowrap;
  }
</style>
</head>
<body>
  <main class="card">
    <div class="band band--top"></div>

    <svg class="name-art" viewBox="0 0 1200 741" aria-label="B.R.W">
      <text class="name-art__ghost" x="0" y="573" font-size="560" textLength="1200" lengthAdjust="spacingAndGlyphs">B.R.W</text>
      <text class="name-art__mark" x="32" y="252" font-size="276" textLength="609" lengthAdjust="spacingAndGlyphs">B.R.W</text>
    </svg>

    <address class="contact" style="font-style: normal;">
      <p class="contact__business">B.R.W Brindlewood Auto Detailing</p>
      <p class="contact__street">42 Fenwarra Crs Brindlewood Vic 3799</p>
      <p class="contact__phones">Ph:(03)59284736 Mob:0417362958</p>
    </address>

    <div class="band band--bottom"></div>
  </main>
</body>
</html>
```